Lumavault Web Design Project

We need a new web page for our startup company based in San Jose, CA called Lumavault.
Lumavault is a web application that helps small businesses share confidential information with their employees, customers, and partners.
With Lumavault, you can share files, bookmarks, and videos on a 'custom' web page that has your logo and that you can host on your servers or on ours. We allow our customers to maintain control of the user experience during sharing by sharing online without sending users to a third-party branded site such as stackpail, crate.io or Orbis cache. Lumavault notifies you know when someone views your content and allows you to recall shared items and email anytime.

"Lumavault can be likened to a secure stackpail with visibility and control of the user experience and on the content that is shared"

We would like to see designs that uses green and black as in the colors on our website www.lumavault.example.
The final design should communicate:
* Secure, Gives Control, Fast, Reliable, Safe, Simple, Flexible, Connects from any device, empower, works on mobile, anywhere, and helpful.

Target Market(s)

Accountants, Financial Advisors, Small Businesses, Start up companies that need to share confidential information online

Industry/Entity Type

It Company

Font styles to use
Sans Serif

Requirements
Must have
• tells customers that they can customize the cloud experience for their users and that they can share online with confidence. Design must be responsive - i.e. should automatically resize itself for viewing on mobile devices
Should not have
• Show secure concept without using a lock image. we feel that lock is old school and does not necessarily show flexibility - we would like to show flexibility with control

```html
<!DOCTYPE html>
<html lang="en">
<head>
<meta charset="utf-8">
<title>Lumavault — Share online with confidence</title>
<link href="https://fonts.googleapis.com/css2?family=Nunito:wght@300;400;600;700&family=Open+Sans:wght@400;600&display=swap" rel="stylesheet">
<style>
:root{
  --green:#3c9a4f;
  --green-light:#4fb063;
  --black:#1c1c1c;
  --ink:#2a2a2a;
  --text:#555;
  --muted:#9a9a9a;
  --line:#e6e6e6;
  --band:#f6f5f1;
  --footer:#1c1c1c;
  --white:#fff;
}
*{margin:0;padding:0;box-sizing:border-box}
html,body{width:711px;height:1200px;overflow:hidden;background:var(--white)}
body{position:relative;font-family:"Open Sans",sans-serif;color:var(--text)}

/* header */
.site-header{position:absolute;left:0;top:0;width:711px;height:61px;border-bottom:1px solid var(--line)}
.brand{position:absolute;left:88px;top:12px;display:flex;align-items:center;gap:8px}
.brand-mark{width:30px;height:30px;border-radius:50%;background:var(--black)}
.brand-text{display:flex;flex-direction:column}
.brand-name{font-family:"Nunito",sans-serif;font-weight:700;font-size:21px;color:var(--ink);line-height:22px}
.brand-tag{font-size:5.5px;color:var(--muted);margin-left:36px;line-height:8px}
.main-nav{position:absolute;top:27px;font-family:"Nunito",sans-serif;font-size:9.5px;color:var(--ink);font-weight:600}
.btn{position:absolute;top:25px;height:18px;font-family:"Nunito",sans-serif;font-size:8.5px;display:flex;align-items:center;justify-content:center}
.btn-login{left:519px;width:48px;background:var(--green);color:var(--white)}
.btn-signup{left:572px;width:48px;border:1px solid #cfcfcf;color:var(--ink);background:#fafafa}

/* hero */
.hero{position:absolute;left:0;top:61px;width:711px;height:285px;background:linear-gradient(100deg,#f4f4f4 0%,#ececec 35%,#e9d6cf 60%,#d9866e 85%,#e3a08b 100%)}
.hero-card{position:absolute;left:86px;top:142px;width:224px;height:106px;background:var(--green);border-bottom:3px solid var(--black);padding:17px 21px;color:var(--white)}
.hero-card h1{font-family:"Nunito",sans-serif;font-weight:400;font-size:20px;line-height:22px}
.hero-card h2{font-family:"Nunito",sans-serif;font-weight:300;font-size:15px;line-height:18px}
.hero-card p{font-size:6.4px;line-height:10px;margin-top:4px;color:#e6f4e8}
.hero-arrow{position:absolute;top:166px}

/* section titles */
.section-title{position:absolute;left:0;width:711px;text-align:center;font-family:"Nunito",sans-serif;font-weight:400;font-size:19px;color:var(--ink)}

/* features */
.feature{position:absolute;width:180px;height:70px}
.feature-icon{position:absolute;left:0;top:0;width:48px;height:48px;border-radius:50%;border:2px solid #e1e1e1;background:var(--white);display:flex;align-items:center;justify-content:center}
.feature-body{position:absolute;left:52px;top:-4px;width:124px}
.feature-body h3{font-family:"Nunito",sans-serif;font-weight:400;font-size:10.5px;color:var(--ink);margin-bottom:3px}
.feature-body p{font-size:6.2px;line-height:10px;color:var(--muted)}
.feature-body a{display:block;margin-top:3px;font-size:7px;font-weight:600;color:var(--green);text-decoration:none}

/* pricing */
.pricing{position:absolute;left:0;top:602px;width:711px;height:240px;background:var(--band);border-top:1px solid var(--line)}
.pricing-sub{position:absolute;left:0;top:60px;width:711px;text-align:center;font-size:7.5px;color:var(--muted)}
.plan{position:absolute;top:84px;height:106px;background:var(--white);box-shadow:0 1px 3px rgba(0,0,0,.1);text-align:center}
.plan-head{height:24px;background:linear-gradient(var(--green-light),var(--green));color:var(--white);font-family:"Nunito",sans-serif;font-weight:700;font-size:9.5px;line-height:24px;border-radius:0 0 50% 50%/0 0 6px 6px}
.plan-price{font-family:"Nunito",sans-serif;font-size:20px;color:var(--ink);margin-top:14px}
.plan-price sup{font-size:8px;vertical-align:10px}
.plan-price small{font-size:10px}
.plan-size{font-size:8.5px;color:#666;margin-top:6px}
.plan.featured{top:81px;height:117px;z-index:2;box-shadow:0 1px 5px rgba(0,0,0,.15)}
.plan.featured .plan-head{background:var(--black);height:27px;line-height:27px;font-size:10px}

/* about */
.about-mission{position:absolute;left:0;top:895px;width:711px;text-align:center;font-size:8.5px;color:var(--green)}
.about-text{position:absolute;left:120px;top:912px;width:472px;text-align:center;font-size:6.6px;line-height:13px;color:#666}
.about-card{position:absolute;top:972px;width:147px}
.about-photo{width:147px;height:64px}
.about-card h3{font-family:"Nunito",sans-serif;font-weight:400;font-size:11px;color:var(--green);margin-top:6px}
.about-card p{font-size:6.3px;line-height:11.5px;color:#666;margin-top:2px}

/* footer */
.site-footer{position:absolute;left:0;top:1130px;width:711px;height:70px;background:var(--footer)}
.footer-links{position:absolute;left:94px;top:19px;font-family:"Nunito",sans-serif;font-size:8.5px;color:var(--white)}
.footer-copy{position:absolute;left:94px;top:37px;font-size:6.8px;color:#aaa}
.social{position:absolute;top:19px;width:13px;height:13px;border-radius:2px;background:var(--green)}
</style>
</head>
<body>

<header class="site-header">
  <div class="brand">
    <span class="brand-mark"></span>
    <div class="brand-text">
      <span class="brand-name">lumavault</span>
      <span class="brand-tag">share online with confidence</span>
    </div>
  </div>
  <nav>
    <span class="main-nav" style="left:296px">Why Lumavault</span>
    <span class="main-nav" style="left:382px">Pricing</span>
    <span class="main-nav" style="left:429px">About</span>
    <span class="main-nav" style="left:472px">Connect</span>
  </nav>
  <span class="btn btn-login">Login</span>
  <span class="btn btn-signup">Sign Up</span>
</header>

<section class="hero" role="img" aria-label="Photo of hands using a smartphone with app icons above a white keyboard"></section>
<div class="hero-card">
  <h1>Lumavault help to</h1>
  <h2>Share files &amp; bookmarks</h2>
  <p>Curabitur iaculis tempus eros Curabitur vel mi sit amet magna malesuada ultrices Ut nisi erat fermentu</p>
</div>
<svg class="hero-arrow" style="left:40px" width="20" height="50" viewBox="0 0 20 50"><polyline points="19,1 1,25 19,49" fill="none" stroke="#444" stroke-width="1"/></svg>
<svg class="hero-arrow" style="left:644px" width="20" height="50" viewBox="0 0 20 50"><polyline points="1,1 19,25 1,49" fill="none" stroke="#444" stroke-width="1"/></svg>

<h2 class="section-title" style="top:372px">Why Lumavault?</h2>

<div class="feature" style="left:86px;top:416px">
  <div class="feature-icon"><svg width="26" height="26" viewBox="0 0 26 26"><circle cx="9" cy="8" r="5" fill="var(--green)"/><path d="M2 24c0-6 3-9 7-9s5 2 6 4" fill="var(--green)"/><circle cx="19" cy="16" r="3" fill="none" stroke="var(--green)" stroke-width="2"/><path d="M17 18l-5 5m2-2l2 2" stroke="var(--green)" stroke-width="2"/></svg></div>
  <div class="feature-body"><h3>Protect your documents</h3><p>Curabitur iaculis tempus eros Curabitur vel mi sit amet magna malesuada ultri-ces Ut nisi erat fermentum</p><a>Read More ›</a></div>
</div>
<div class="feature" style="left:270px;top:416px">
  <div class="feature-icon"><svg width="26" height="26" viewBox="0 0 26 26"><path d="M4 9v13h16v-5" fill="none" stroke="var(--green)" stroke-width="2.4"/><path d="M9 17c0-6 4-9 10-9V4l6 6-6 6v-4c-4 0-7 1-10 5z" fill="var(--green)"/></svg></div>
  <div class="feature-body"><h3>Safe Place to Share</h3><p>Curabitur iaculis tempus eros Curabitur vel mi sit amet magna malesuada ultri-ces Ut nisi erat fermentum</p><a>Read More ›</a></div>
</div>
<div class="feature" style="left:455px;top:416px">
  <div class="feature-icon"><svg width="26" height="26" viewBox="0 0 26 26"><path d="M9 3l4 3 4-3-2 5h-4z" fill="var(--green)"/><path d="M10 9h6c5 3 7 8 6 11-1 3-4 4-9 4s-8-1-9-4c-1-3 1-8 6-11z" fill="var(--green)"/><text x="13" y="21" text-anchor="middle" font-size="10" font-family="Open Sans,sans-serif" fill="#fff" font-weight="600">$</text></svg></div>
  <div class="feature-body"><h3>Save Your Money</h3><p>Curabitur iaculis tempus eros Curabitur vel mi sit amet magna malesuada ultri-ces Ut nisi erat fermentum</p><a>Read More ›</a></div>
</div>
<div class="feature" style="left:86px;top:505px">
  <div class="feature-icon"><svg width="26" height="26" viewBox="0 0 26 26"><g stroke="var(--green)" stroke-width="2" stroke-linecap="round"><line x1="4" y1="6" x2="22" y2="6"/><line x1="4" y1="13" x2="22" y2="13"/><line x1="4" y1="20" x2="22" y2="20"/></g><g fill="var(--white)" stroke="var(--green)" stroke-width="2"><circle cx="9" cy="6" r="2.6"/><circle cx="17" cy="13" r="2.6"/><circle cx="11" cy="20" r="2.6"/></g></svg></div>
  <div class="feature-body"><h3>Content Security</h3><p>Curabitur iaculis tempus eros Curabitur vel mi sit amet magna malesuada ultri-ces Ut nisi erat fermentum</p><a>Read More ›</a></div>
</div>
<div class="feature" style="left:270px;top:505px">
  <div class="feature-icon"><svg width="28" height="28" viewBox="0 0 28 28"><g stroke="var(--green)" stroke-width="1.5"><line x1="14" y1="14" x2="4" y2="9"/><line x1="14" y1="14" x2="13" y2="3"/><line x1="14" y1="14" x2="25" y2="11"/><line x1="14" y1="14" x2="6" y2="23"/><line x1="14" y1="14" x2="21" y2="24"/></g><g fill="var(--green)"><circle cx="14" cy="14" r="4"/><circle cx="4" cy="9" r="2.5"/><circle cx="13" cy="3" r="2.5"/><circle cx="25" cy="11" r="2.5"/><circle cx="6" cy="23" r="2.5"/><circle cx="21" cy="24" r="2.5"/></g></svg></div>
  <div class="feature-body"><h3>Network Protection</h3><p>Curabitur iaculis tempus eros Curabitur vel mi sit amet magna malesuada ultri-ces Ut nisi erat fermentum</p><a>Read More ›</a></div>
</div>
<div class="feature" style="left:455px;top:505px">
  <div class="feature-icon"><svg width="28" height="26" viewBox="0 0 28 26"><rect x="10" y="3" width="8" height="5" fill="none" stroke="var(--green)" stroke-width="2"/><rect x="2" y="7" width="24" height="16" rx="1" fill="var(--green)"/><rect x="2" y="13" width="24" height="1.5" fill="#fff"/></svg></div>
  <div class="feature-body"><h3>Business Efficiency</h3><p>Curabitur iaculis tempus eros Curabitur vel mi sit amet magna malesuada ultri-ces Ut nisi erat fermentum</p><a>Read More ›</a></div>
</div>

<section class="pricing">
  <h2 class="section-title" style="top:28px">Our Pricing</h2>
  <p class="pricing-sub">Morbi ornare gravida elit Integer congue augue et malesuada iaculis ipsum dui aliquet felis at</p>
  <div class="plan" style="left:106px;width:116px"><div class="plan-head">Basic Plan</div><div class="plan-price" style="font-weight:600">FREE</div><div class="plan-size">1.5 GB</div></div>
  <div class="plan featured" style="left:222px;width:128px"><div class="plan-head">Individuals</div><div class="plan-price" style="margin-top:16px"><sup>$</sup>6.95/<small>mo</small></div><div class="plan-size">10 GB</div></div>
  <div class="plan" style="left:350px;width:115px"><div class="plan-head">Small Business</div><div class="plan-price"><sup>$</sup>49.95/<small>mo</small></div><div class="plan-size">50 GB</div></div>
  <div class="plan" style="left:465px;width:117px"><div class="plan-head">Enterprise</div><div class="plan-price"><sup>$</sup>150.00/<small>mo</small></div><div class="plan-size">Unlimited</div></div>
</section>

<h2 class="section-title" style="top:867px">About Our Company</h2>
<p class="about-mission">Lumavault's mission is to simplify and secure online collaboration.</p>
<p class="about-text">Many services now exist for sharing your personal or corporate information online. The question is whether or not your information is secure and protected, and how much control you have over the information you share. Lumavault was established specifically to address this concern. Our Mission is to provide secure messaging channels to allow individuals, businesses, institutions and governments to securely communicate with their collaborators.</p>

<div class="about-card" style="left:116px">
  <div class="about-photo" role="img" aria-label="Photo of a person in front of a chalkboard with sketched devices" style="background:linear-gradient(135deg,#6f7370,#4a4e4c)"></div>
  <h3>Turnkey Solution</h3>
  <p>Lumavault requires no software to down-load or install, reducing the hassle for all end users. It is simple intuitive and effective</p>
</div>
<div class="about-card" style="left:282px">
  <div class="about-photo" role="img" aria-label="Photo of a support team with headsets at computer desks" style="background:linear-gradient(135deg,#e4e4e2,#9a9c9b)"></div>
  <h3>Technical Support</h3>
  <p>Lumavault requires no software to down-load or install, reducing the hassle for all end users. It is simple intuitive and effective</p>
</div>
<div class="about-card" style="left:445px">
  <div class="about-photo" role="img" aria-label="Photo of a smiling businessman in a modern glass office" style="background:linear-gradient(135deg,#5d4a3e,#a9b6bd)"></div>
  <h3>Worldwide Presence</h3>
  <p>Lumavault requires no software to down-load or install, reducing the hassle for all end users. It is simple intuitive and effective</p>
</div>

<footer class="site-footer">
  <nav class="footer-links">Why Lumavault? &nbsp;|&nbsp; Pricing &nbsp;|&nbsp; About &nbsp;|&nbsp; Connect &nbsp;|&nbsp; Terms and Conditions &nbsp;|&nbsp; Privacy Policy</nav>
  <p class="footer-copy">© 2014 Company Name &nbsp;All right reserved &nbsp;Term of Use</p>
  <span class="social" style="left:561px" aria-label="Social link"></span>
  <span class="social" style="left:580px" aria-label="Social link"></span>
  <span class="social" style="left:599px" aria-label="Social link"></span>
</footer>

</body>
</html>
```